LumaVantix
stationery - business cards
LumaVantix -
Creative Brief
Professional
Carl MORVEDO
41 Pellin Lane, suite 218 Corvell, Oregon, 97321
cm@lumavantix.com
www.lumavantix.com
Free to be creative

```html
<!DOCTYPE html>
<html lang="en">
<head>
<meta charset="utf-8">
<title>LumaVantix Stationery</title>
<link rel="stylesheet" href="https://fonts.googleapis.com/css2?family=Source+Sans+3:wght@400;600&display=swap">
<style>
  :root {
    --brand-blue: #2b4c9e;
    --brand-blue-dark: #1f3a80;
    --ink: #333333;
    --paper: #ffffff;
    --line: #cfcfcf;
    --soft-grey: #eeeff2;
    --soft-blue: #e4e9f3;
    --stage: #ffffff;
  }
  * { box-sizing: border-box; margin: 0; padding: 0; }
  html, body { width: 1200px; height: 701px; overflow: hidden; background: var(--stage); }
  body { font-family: "Source Sans 3", Arial, sans-serif; color: var(--ink); position: relative; }

  .piece { position: absolute; background: var(--paper); border: 1px solid var(--line); box-shadow: 0 1px 3px rgba(0,0,0,.12); overflow: hidden; }

  .wordmark { display: flex; align-items: center; gap: 8px; font-weight: 600; color: var(--brand-blue); letter-spacing: .5px; white-space: nowrap; }
  .wordmark__square { display: block; background: currentColor; }

  /* Business card front */
  .card-front { left: 48px; top: 84px; width: 288px; height: 168px; }
  .card-front__name { position: absolute; left: 36px; top: 52px; font-size: 15px; }
  .card-front__contact { position: absolute; left: 36px; top: 98px; font-size: 6.5px; line-height: 1.35; }
  .label { color: var(--brand-blue); font-weight: 600; }
  .card-front__accent { position: absolute; right: 14px; top: 10px; width: 62px; height: 148px; border-radius: 8px;
    background: linear-gradient(180deg, var(--brand-blue) 0%, #7d8aa8 48%, #9a9a9a 60%, #6f6f6f 100%); }

  /* Business card back */
  .card-back { left: 360px; top: 84px; width: 252px; height: 168px; border: none;
    background: linear-gradient(135deg, var(--brand-blue) 0%, var(--brand-blue-dark) 100%); }
  .card-back__accent { position: absolute; left: 0; top: 0; width: 64px; height: 120px;
    background: linear-gradient(180deg, rgba(255,255,255,.25), rgba(255,255,255,.08)); border-radius: 0 0 8px 0; }
  .card-back .wordmark { position: absolute; left: 82px; top: 66px; font-size: 24px; color: #ffffff; }
  .card-back .wordmark__square { width: 18px; height: 18px; }
  .card-back__web { position: absolute; right: 12px; bottom: 8px; font-size: 5.5px; color: #c9d3ec; }

  /* Envelope */
  .envelope { left: 19px; top: 288px; width: 593px; height: 384px; }
  .envelope__flap { position: absolute; left: 0; top: 0; }
  .envelope__seal { position: absolute; left: 287px; top: 26px; width: 18px; height: 18px; background: #8a8a8a; }
  .envelope .wordmark { position: absolute; left: 18px; top: 90px; font-size: 26px; }
  .envelope .wordmark__square { width: 20px; height: 20px; }
  .contact-block { font-size: 10px; line-height: 1.4; }
  .envelope .contact-block { position: absolute; left: 18px; bottom: 14px; }
  .faint-decor { position: absolute; border-radius: 14px;
    background: linear-gradient(135deg, var(--soft-blue) 0%, var(--soft-grey) 60%, #f7f7f8 100%); }
  .envelope .faint-decor { right: 0; bottom: 0; width: 210px; height: 150px; border-radius: 14px 0 0 0; }

  /* Letterhead */
  .letterhead { left: 679px; top: 19px; width: 497px; height: 660px; }
  .letterhead .wordmark { position: absolute; left: 22px; top: 26px; font-size: 26px; }
  .letterhead .wordmark__square { width: 20px; height: 20px; }
  .letterhead .contact-block { position: absolute; right: 22px; top: 26px; text-align: right; }
  .letterhead .faint-decor { right: 0; bottom: 0; width: 210px; height: 200px; border-radius: 14px 0 0 0; }
</style>
</head>
<body>

  <section class="piece card-front">
    <p class="card-front__name">Carl MORVEDO</p>
    <div class="card-front__contact">
      <p>41 Pellin Lane, suite 218</p>
      <p>Corvell, Oregon, 97321</p>
      <p><span class="label">Phone:</span> 800 555 0147</p>
      <p><span class="label">Email:</span> cm@lumavantix.com</p>
    </div>
    <div class="card-front__accent" role="img" aria-label="Brand accent panel in blue and grey"></div>
  </section>

  <section class="piece card-back">
    <div class="card-back__accent" role="img" aria-label="Brand accent panel"></div>
    <div class="wordmark"><span class="wordmark__square"></span>LumaVantix</div>
    <p class="card-back__web">www.lumavantix.com</p>
  </section>

  <section class="piece envelope">
    <svg class="envelope__flap" width="593" height="100" viewBox="0 0 593 100" aria-hidden="true">
      <polyline points="0,0 296,84 593,0" fill="none" stroke="#d6d6d6" stroke-width="1"/>
    </svg>
    <span class="envelope__seal"></span>
    <div class="wordmark"><span class="wordmark__square"></span>LumaVantix</div>
    <div class="contact-block">
      <p>41 Pellin Lane, suite 218</p>
      <p>Corvell, Oregon, 97321</p>
      <p><span class="label">Phone:</span> 800 555 0147</p>
      <p><span class="label">Email:</span> cm@lumavantix.com</p>
    </div>
    <div class="faint-decor" role="img" aria-label="Faint brand decoration"></div>
  </section>

  <section class="piece letterhead">
    <div class="wordmark"><span class="wordmark__square"></span>LumaVantix</div>
    <div class="contact-block">
      <p>41 Pellin Lane, suite 218</p>
      <p>Corvell, Oregon, 97321</p>
      <p><span class="label">Phone:</span> 800 555 0147</p>
    </div>
    <div class="faint-decor" role="img" aria-label="Faint brand decoration"></div>
  </section>

</body>
</html>
```